Velmora Biz Card 2019

New business card for Velmora Property Inspections. We are a residential home inspection company in Arizona.

Target Market(s)

Real Estate

Font styles to use
Sans Serif

Requirements
Must have
• Glen Mirewick
• Home Inspector
• Velmora Property Inspections, LLC
• 480-555-0172
• glen@velmora-llc.example

```html
<!DOCTYPE html>
<html lang="en">
<head>
<meta charset="utf-8">
<title>Velmora Biz Card 2019</title>
<link href="https://fonts.googleapis.com/css2?family=Open+Sans:wght@400;700&display=swap" rel="stylesheet">
<style>
  :root {
    --page-bg: #e4e2df;
    --card-bg: #0d0d0d;
    --brand-green: #3fae3a;
    --text-light: #f2f2f2;
    --mark-grey: #e6e6e6;
  }
  html, body {
    margin: 0;
    padding: 0;
    width: 1200px;
    height: 1200px;
    overflow: hidden;
    background: var(--page-bg);
    font-family: "Open Sans", Arial, sans-serif;
  }
  .business-card {
    position: absolute;
    left: 100px;
    top: 314px;
    width: 1000px;
    height: 572px;
    background: var(--card-bg);
    box-shadow: 0 10px 30px rgba(0,0,0,0.25);
  }
  .contact-block {
    position: absolute;
    left: 96px;
    top: 250px;
    color: var(--text-light);
  }
  .person-name {
    margin: 0;
    font-size: 46px;
    font-weight: 700;
    line-height: 1;
    color: var(--brand-green);
  }
  .person-role {
    margin: 6px 0 0 36px;
    font-size: 22px;
    line-height: 1.2;
  }
  .company-details {
    margin: 30px 0 0 36px;
    font-size: 21px;
    line-height: 1.3;
  }
  .company-name { color: var(--brand-green); }
  .contact-lines {
    margin: 34px 0 0 36px;
    font-size: 21px;
    line-height: 1.4;
  }
  .contact-line {
    display: flex;
    align-items: center;
    gap: 10px;
  }
  .contact-icon { width: 16px; height: 16px; flex: none; }
  .brand-mark {
    position: absolute;
    left: 620px;
    top: 235px;
    display: flex;
    align-items: center;
    gap: 16px;
  }
  .brand-square {
    width: 34px;
    height: 34px;
    background: var(--brand-green);
  }
  .brand-name {
    font-size: 62px;
    font-weight: 700;
    letter-spacing: 3px;
    color: var(--mark-grey);
    line-height: 1;
  }
</style>
</head>
<body>
  <div class="business-card">
    <div class="brand-mark">
      <span class="brand-square"></span>
      <span class="brand-name">VELMORA</span>
    </div>
    <div class="contact-block">
      <h1 class="person-name">Glen Mirewick</h1>
      <div class="person-role">Home Inspector</div>
      <div class="company-details">
        <div class="company-name">Velmora Property Inspections, LLC</div>
        <div class="company-address">10450 S. 48th St. Tempe, AZ 85283</div>
      </div>
      <div class="contact-lines">
        <div class="contact-line">
          <svg class="contact-icon" viewBox="0 0 16 16" aria-hidden="true">
            <path d="M3 1.5 L6 1.5 L7 5 L5.2 6.3 C6 8.2 7.8 10 9.7 10.8 L11 9 L14.5 10 L14.5 13 C14.5 14 13.7 14.5 13 14.5 C6.5 14 2 9.5 1.5 3 C1.5 2.3 2 1.5 3 1.5 Z" fill="var(--brand-green)"/>
          </svg>
          <span>+480-555-0172</span>
        </div>
        <div class="contact-line">
          <svg class="contact-icon" viewBox="0 0 16 16" aria-hidden="true">
            <rect x="1" y="3" width="14" height="10" fill="var(--brand-green)"/>
            <path d="M1 3 L8 9 L15 3" fill="none" stroke="var(--card-bg)" stroke-width="1.4"/>
          </svg>
          <span>glen@velmora-llc.example</span>
        </div>
      </div>
    </div>
  </div>
</body>
</html>
```